CaptainKettle needs a new packaging

We are Coffee Roasters based in Versailles France.

We want a new design for our coffee packaging. The packaging is a basic brown paper bag. We are sticking on it a 99.1mm x 67.7mm Label.

We want a new design for the label. The label should have the following info : Name of the coffee, origin, one line of description, our website www.captainkettle.fr.

Enclosed you will find our logo, as well as a picture of our current packaging

The Design should be "simple yet sophisticate".

```html
<!DOCTYPE html>
<html lang="en">
<head>
<meta charset="utf-8">
<title>CaptainKettle – Coffee Label</title>
<link rel="stylesheet" href="https://fonts.googleapis.com/css2?family=Josefin+Sans:wght@300;400&family=Michroma&display=swap">
<style>
  :root {
    --ink: #121416;
    --ink-soft: #1a1c1f;
    --copy-blue: #1d4a70;
    --white: #ffffff;
    --grey-dark: #5a5a5a;
    --grey-mid: #9a9a9a;
    --grey-light: #d9d9d9;
    --teal-deep: #0f4a66;
    --teal-mid: #2a7f9c;
    --teal-light: #8fc6cf;
    --bean-dark: #1a1416;
    --bean-brown: #5a4038;
    --swatch-red: #b8473a;
    --swatch-tan: #c99a6a;
    --swatch-brown: #6b3a2e;
  }
  html, body {
    margin: 0;
    padding: 0;
    width: 1200px;
    height: 819px;
    overflow: hidden;
    background: #ffffff;
  }
  .label {
    position: relative;
    width: 1200px;
    height: 819px;
    overflow: hidden;
  }
  .photo-sky {
    position: absolute;
    left: 0; top: 0;
    width: 616px; height: 819px;
    background:
      radial-gradient(ellipse 420px 160px at 250px 680px, rgba(255,255,255,0.75), transparent 70%),
      linear-gradient(180deg, var(--grey-dark) 0%, var(--grey-mid) 45%, var(--grey-light) 70%, var(--grey-mid) 100%);
  }
  .photo-bean {
    position: absolute;
    left: 616px; top: 0;
    width: 584px; height: 819px;
    background:
      radial-gradient(ellipse 260px 140px at 290px 500px, var(--bean-dark) 0%, var(--bean-brown) 45%, transparent 75%),
      radial-gradient(ellipse 420px 160px at 300px 660px, var(--teal-light), transparent 75%),
      linear-gradient(180deg, var(--teal-deep) 0%, var(--teal-mid) 55%, var(--teal-light) 100%);
  }
  .brand-name {
    position: absolute;
    left: 278px; top: 60px;
    width: 916px;
    margin: 0;
    font-family: "Josefin Sans", sans-serif;
    font-weight: 400;
    font-size: 112px;
    line-height: 1;
    color: var(--ink);
    text-transform: uppercase;
    white-space: nowrap;
    letter-spacing: -1px;
  }
  .brand-mark {
    position: absolute;
    left: 20px; top: 20px;
    width: 210px; height: 300px;
    border-radius: 50%;
    background: var(--ink);
  }
  .brand-rule {
    position: absolute;
    left: 280px; top: 226px;
    width: 912px; height: 6px;
    background: var(--ink);
  }
  .tagline {
    position: absolute;
    left: 288px; top: 256px;
    margin: 0;
    font-family: "Josefin Sans", sans-serif;
    font-weight: 300;
    font-size: 58px;
    line-height: 1;
    color: var(--ink-soft);
    white-space: nowrap;
  }
  .roast-swatches {
    position: absolute;
    left: 934px; top: 262px;
    width: 220px; height: 64px;
  }
  .copy {
    position: absolute;
    left: 0; width: 600px;
    margin: 0;
    font-family: "Michroma", sans-serif;
    font-size: 20px;
    line-height: 41px;
    letter-spacing: 3px;
    color: var(--copy-blue);
    text-align: center;
    text-transform: uppercase;
  }
  .copy-morning { top: 448px; }
  .copy-origin { top: 580px; font-size: 22px; line-height: 46px; }
  .website {
    position: absolute;
    right: 28px; top: 762px;
    margin: 0;
    font-family: "Michroma", sans-serif;
    font-size: 19px;
    letter-spacing: 3px;
    color: var(--white);
    text-transform: uppercase;
  }
</style>
</head>
<body>
<main class="label">
  <div class="photo-sky" role="img" aria-label="Grey cloudy sky photograph"></div>
  <div class="photo-bean" role="img" aria-label="Close-up photograph of a roasted coffee bean with water droplets on a blue background"></div>

  <div class="brand-mark"></div>
  <h1 class="brand-name">CaptainKettle</h1>
  <div class="brand-rule"></div>
  <p class="tagline">Artisan Torréfacteur</p>

  <svg class="roast-swatches" viewBox="0 0 220 64" role="img" aria-label="Three coffee bean illustrations in light, medium and dark roast">
    <ellipse cx="36" cy="32" rx="36" ry="29" fill="var(--swatch-red)"/>
    <ellipse cx="110" cy="32" rx="36" ry="29" fill="var(--swatch-tan)"/>
    <ellipse cx="184" cy="32" rx="36" ry="29" fill="var(--swatch-brown)"/>
  </svg>

  <p class="copy copy-morning">All you need for your morning<br>is this fine arabica coffe.</p>
  <p class="copy copy-origin">Imported all the way from<br>farms of (Bresil, Congo,<br>and Ethiopic</p>

  <p class="website">www.captainkettle.fr</p>
</main>
</body>
</html>
```